WP website design (Brenn)

We need a wordpress design for an established auction and real estate company based in Tennessee. The winning design will incorporate a professional color scheme with company logo in a clean layout. The design needs to consider that this will be developed on a responsive theme. Colors are those that will highlight the logo.

Industry/Entity Type

Real Estate

Font styles to use
Sans Serif

Colors

Designer to choose colors to be used in the design.

Requirements
Must have
• Navigation: 1) Home - with auctions as content as seen at http://vornelbidhouse.com/ 2) Current Auctions 3) Past Auctions 4) Referrals 5) Why Auction 6) About Us 7) Contact Us

Header will have logo, contact info, Social icons (Facebook, Twitter, Youtube) and tagline "Bid Smart With Brenn!' Slideshow (use stock real estate image for image) will be used either in header or content area.

Widgets: Email signup form, Upcoming Auctions, Register for Online Bidding text, testimonials

Footer will have contact info (below) smaller company logo, and the association logos attached.

```html
<!DOCTYPE html>
<html lang="en">
<head>
<meta charset="utf-8">
<title>Brenn Realty &amp; Auction</title>
<link href="https://fonts.googleapis.com/css2?family=Open+Sans:wght@400;600;700&family=Roboto+Condensed:wght@400;700&display=swap" rel="stylesheet">
<style>
:root{
  --green:#5f8c3a;
  --green-bright:#8cc63f;
  --nav-green:#6b9a46;
  --navy:#2f3350;
  --slider-bg:#2b2b30;
  --text:#444;
  --muted:#666;
  --link:#1f5fae;
  --border:#cfcfcf;
  --input-border:#bbb;
  --white:#fff;
}
*{box-sizing:border-box;margin:0;padding:0}
html,body{width:1200px;height:2691px;overflow:hidden;background:var(--white)}
body{position:relative;font-family:"Open Sans",Arial,sans-serif;color:var(--text);font-size:13px}
.cond{font-family:"Roboto Condensed","Arial Narrow",sans-serif}

/* Header */
.site-header{position:absolute;left:0;top:0;width:1200px;height:145px}
.brand{position:absolute;left:85px;top:30px;display:flex;align-items:center;gap:14px}
.brand-mark{width:44px;height:44px;background:var(--green)}
.brand-name{font-family:"Roboto Condensed",sans-serif;font-weight:700;font-size:60px;color:var(--green);line-height:1}
.contact-strip{position:absolute;top:12px;right:60px;display:flex;align-items:center;gap:14px;font-family:"Roboto Condensed",sans-serif;font-weight:700;font-size:15px;color:var(--green)}
.social{display:flex;gap:8px;margin-right:18px}
.social span{width:24px;height:24px;background:var(--navy);display:block}
.social span:nth-child(2){background:var(--nav-green)}
.social span:nth-child(3){background:#8a8f99}
.call{color:var(--green)}
.call b{color:var(--navy)}
.tagline{position:absolute;right:18px;top:62px;font-family:"Roboto Condensed",sans-serif;font-weight:700;font-size:46px;color:var(--navy)}

/* Navigation */
.main-nav{position:absolute;left:0;top:145px;width:1200px;height:68px;background:var(--nav-green)}
.main-nav ul{list-style:none;position:relative;height:68px}
.main-nav li{position:absolute;top:0;height:68px;line-height:68px;color:var(--white);font-size:16px}
.main-nav li.active{background:var(--navy);text-align:center}
.main-nav .sep{color:rgba(255,255,255,.8)}

/* Slider */
.hero{position:absolute;left:0;top:213px;width:1200px;height:469px;background:var(--slider-bg)}
.hero-photo{position:absolute;left:70px;top:6px;width:1060px;height:455px;background:linear-gradient(180deg,#9db8cf 0%,#c9d6df 38%,#e6e6e2 55%,#7d8c72 75%,#4f6b3a 100%)}
.hero-caption{position:absolute;left:92px;top:394px;font-family:"Roboto Condensed",sans-serif;font-weight:700;font-size:42px;color:var(--green-bright)}
.hero-arrow{position:absolute;top:220px}
.hero-arrow.prev{left:28px}
.hero-arrow.next{right:28px}

/* Section heading & pager */
.section-title{position:absolute;left:78px;top:694px;font-family:"Roboto Condensed",sans-serif;font-weight:700;font-size:32px;color:var(--green)}
.pager{position:absolute;display:flex;gap:4px}
.pager span{display:block;height:26px;line-height:26px;padding:0 9px;background:#1f1f24;color:var(--white);font-size:12px;font-weight:600}
.pager span.current{background:#4a4a52}

/* Auction cards */
.auction-list{position:absolute;left:78px;top:752px;width:648px}
.auction-card{height:320px;border:1px solid var(--border);padding:6px 7px;margin-bottom:17px;position:relative}
.auction-card h3{height:40px;line-height:40px;background:var(--navy);color:var(--white);font-size:17px;font-weight:700;padding-left:14px}
.auction-media{position:absolute;left:8px;top:78px;width:246px;height:193px}
.auction-photo{height:159px;background:linear-gradient(180deg,#a9c3d8 0%,#d4dde3 35%,#b9b3a6 60%,#5f7a45 100%)}
.details-bar{height:34px;background:var(--navy);color:var(--white);font-size:13px;font-weight:600;display:flex;align-items:center;justify-content:space-between;padding:0 8px 0 14px}
.auction-info{position:absolute;left:268px;top:58px;width:366px}
.auction-info h4{color:var(--green);font-size:14px;font-weight:700}
.auction-info p.summary{color:var(--muted);font-size:12.5px;line-height:17px;margin-top:6px}
.auction-info hr{border:0;border-top:1px solid #ddd;margin:9px 0 10px}
.auction-info .mode{color:var(--green);font-size:14px;font-weight:700;margin-bottom:10px}
.auction-info .begins{font-size:13px;color:var(--navy);font-weight:700}
.auction-info .begins span{color:var(--link);font-weight:400}
.auction-info .loc{margin-top:8px;font-size:12.5px;line-height:17px;color:var(--navy)}
.auction-info .loc b{display:block}
.bid-btn{position:absolute;left:268px;top:262px;width:250px;height:40px;background:var(--green);color:var(--white);font-size:13px;font-weight:600;display:flex;align-items:center;justify-content:space-between;padding:0 10px 0 14px}
.results-count{position:absolute;left:78px;top:2440px;color:var(--green);font-weight:700;font-size:14px}

/* Sidebar */
.sidebar{position:absolute;left:765px;top:752px;width:355px}
.widget{border:1px solid var(--border);padding:6px 7px;position:absolute;left:0;width:355px}
.widget h2{height:38px;line-height:38px;background:var(--green);color:var(--white);font-family:"Roboto Condensed",sans-serif;font-weight:700;font-size:21px;padding-left:12px}
.field{display:block;width:305px;height:30px;border:1px solid var(--input-border);font-size:11.5px;color:#999;line-height:28px;padding-left:10px;margin-left:18px}
.btn-navy{display:inline-block;background:var(--navy);color:var(--white);font-size:13px;font-weight:600;height:30px;line-height:30px;padding:0 16px;margin-left:18px}
.widget p.note{font-size:13px;color:var(--text);margin:16px 0 0 18px}
.search-row{display:flex;margin:18px 0 0 10px}
.search-row .field{margin:0;width:280px;height:34px;line-height:32px}
.search-row .go{width:50px;height:34px;background:var(--navy);color:var(--white);font-weight:700;text-align:center;line-height:34px;font-size:15px}
.featured{text-align:center}
.featured h5{font-size:14px;font-weight:700;color:var(--navy);margin-top:14px}
.featured-photo{width:320px;height:132px;margin:10px auto 0;background:linear-gradient(180deg,#8fb1cf 0%,#cfd9e0 35%,#c8b49a 65%,#6b8a4a 100%);border:3px solid var(--navy)}
.featured .name{color:var(--green);font-size:13px;margin-top:8px;font-weight:600}
.featured p{font-size:12px;line-height:16px;color:var(--text);padding:0 14px}
.more-btn{display:block;height:46px;line-height:46px;margin:14px 12px 8px;background:var(--navy);color:var(--white);font-family:"Roboto Condensed",sans-serif;font-weight:700;font-size:21px}
.testimonial{margin:14px 10px 0}
.testimonial h6{color:var(--green);font-size:13px;font-weight:700}
.testimonial p{font-size:12px;line-height:16px;color:var(--text)}
.testimonial a{color:var(--link);font-size:12px;text-decoration:underline;display:inline-block;margin-top:4px}
.testimonial + .testimonial{border-top:1px solid #ddd;padding-top:14px}

/* Footer */
.site-footer{position:absolute;left:0;top:2497px;width:1200px;height:194px;border-top:1px solid #ddd}
.footer-col h2{font-family:"Roboto Condensed",sans-serif;font-weight:700;font-size:16px;color:var(--green)}
.footer-col{position:absolute;top:14px}
.assoc-badges{display:flex;gap:10px;margin-top:22px}
.assoc-badges span{display:block;height:46px;background:#d9d9d9;border:2px solid #555}
.footer-contact p{font-size:12px;line-height:16px;color:var(--text)}
.footer-contact p.gap{margin-top:6px}
.footer-contact a{color:var(--link);text-decoration:none}
.footer-brand{position:absolute;left:620px;top:22px;display:flex;align-items:center;gap:12px}
.footer-brand .brand-mark{width:40px;height:40px}
.footer-brand .brand-name{font-size:58px}
.footer-social{display:flex;gap:8px;margin-top:14px;justify-content:center}
.footer-social span{width:24px;height:24px;display:block;background:var(--navy)}
.footer-social span:nth-child(2){background:var(--nav-green)}
.footer-social span:nth-child(3){background:#8a8f99}
.copyright{position:absolute;left:78px;top:142px;font-size:11px;color:var(--muted)}
</style>
</head>
<body>

<header class="site-header">
  <div class="brand"><span class="brand-mark"></span><span class="brand-name">Brenn</span></div>
  <div class="contact-strip">
    <span>Get In Touch With Us</span>
    <span class="social" aria-label="Social links"><span></span><span></span><span></span></span>
    <span class="call">Call Us : <b>(800) 555-0142</b></span>
  </div>
  <div class="tagline">Bid Smart With Brenn!</div>
</header>

<nav class="main-nav">
  <ul>
    <li class="active" style="left:98px;width:110px">Home</li>
    <li style="left:238px">Current Auctions</li>
    <li class="sep" style="left:392px">|</li>
    <li style="left:420px">Past Auctions</li>
    <li class="sep" style="left:548px">|</li>
    <li style="left:580px">Referrals</li>
    <li class="sep" style="left:682px">|</li>
    <li style="left:710px">Why Auction</li>
    <li class="sep" style="left:832px">|</li>
    <li style="left:862px">About Us</li>
    <li class="sep" style="left:962px">|</li>
    <li style="left:992px">Contact Us</li>
  </ul>
</nav>

<section class="hero">
  <div class="hero-photo" role="img" aria-label="Modern single-storey house with pool and lawn"></div>
  <div class="hero-caption">Lorem ipsum dolsr sit amet</div>
  <svg class="hero-arrow prev" width="20" height="30" viewBox="0 0 20 30"><path d="M15 3 L4 15 L15 27" fill="none" stroke="#fff" stroke-width="4"/></svg>
  <svg class="hero-arrow next" width="20" height="30" viewBox="0 0 20 30"><path d="M5 3 L16 15 L5 27" fill="none" stroke="#fff" stroke-width="4"/></svg>
</section>

<h1 class="section-title">Upcoming Auctions</h1>
<div class="pager" style="left:606px;top:706px"><span class="current">1</span><span>2</span><span>Next</span></div>

<main class="auction-list">
  <article class="auction-card">
    <h3>Lorem ipsum dolor sit amet conse ctetur adipisicing</h3>
    <div class="auction-media">
      <div class="auction-photo" role="img" aria-label="Large two-storey family home"></div>
      <div class="details-bar">Click Here for More Details
        <svg width="22" height="22" viewBox="0 0 22 22"><circle cx="12" cy="9" r="6.5" fill="none" stroke="#fff" stroke-width="2.5"/><path d="M7.5 13.5 L2 19.5" stroke="#fff" stroke-width="3"/></svg></div>
    </div>
    <div class="auction-info">
      <h4>Lorem ipsum dolor sit amet conse ctetur adipisicing</h4>
      <p class="summary">Duis aute irure dolor in reprehenderit in voluptate velit esse cillum dolore eu fugiat.</p>
      <hr>
      <div class="mode">Live Off-site Auction with Online Bidding</div>
      <div class="begins">Begins: <span>Tuesday, December 23, 2014 at 1:00 PM EST</span></div>
      <div class="loc"><b>Location:</b>P.O. Box 41207<br>Maryville, TN 37801</div>
    </div>
    <div class="bid-btn">Click Here for Online Bidding
      <svg width="24" height="20" viewBox="0 0 24 20"><rect x="1.5" y="1.5" width="21" height="13" fill="none" stroke="#fff" stroke-width="2"/><path d="M8 19 H16 M12 15 V19" stroke="#fff" stroke-width="2"/></svg></div>
  </article>

  <article class="auction-card">
    <h3>Lorem ipsum dolor sit amet conse ctetur adipisicing</h3>
    <div class="auction-media">
      <div class="auction-photo" role="img" aria-label="Large two-storey family home"></div>
      <div class="details-bar">Click Here for More Details
        <svg width="22" height="22" viewBox="0 0 22 22"><circle cx="12" cy="9" r="6.5" fill="none" stroke="#fff" stroke-width="2.5"/><path d="M7.5 13.5 L2 19.5" stroke="#fff" stroke-width="3"/></svg></div>
    </div>
    <div class="auction-info">
      <h4>Lorem ipsum dolor sit amet conse ctetur adipisicing</h4>
      <p class="summary">Duis aute irure dolor in reprehenderit in voluptate velit esse cillum dolore eu fugiat.</p>
      <hr>
      <div class="mode">Live Off-site Auction with Online Bidding</div>
      <div class="begins">Begins: <span>Tuesday, December 23, 2014 at 1:00 PM EST</span></div>
      <div class="loc"><b>Location:</b>P.O. Box 41207<br>Maryville, TN 37801</div>
    </div>
    <div class="bid-btn">Click Here for Online Bidding
      <svg width="24" height="20" viewBox="0 0 24 20"><rect x="1.5" y="1.5" width="21" height="13" fill="none" stroke="#fff" stroke-width="2"/><path d="M8 19 H16 M12 15 V19" stroke="#fff" stroke-width="2"/></svg></div>
  </article>

  <article class="auction-card">
    <h3>Lorem ipsum dolor sit amet conse ctetur adipisicing</h3>
    <div class="auction-media">
      <div class="auction-photo" role="img" aria-label="Large two-storey family home"></div>
      <div class="details-bar">Click Here for More Details
        <svg width="22" height="22" viewBox="0 0 22 22"><circle cx="12" cy="9" r="6.5" fill="none" stroke="#fff" stroke-width="2.5"/><path d="M7.5 13.5 L2 19.5" stroke="#fff" stroke-width="3"/></svg></div>
    </div>
    <div class="auction-info">
      <h4>Lorem ipsum dolor sit amet conse ctetur adipisicing</h4>
      <p class="summary">Duis aute irure dolor in reprehenderit in voluptate velit esse cillum dolore eu fugiat.</p>
      <hr>
      <div class="mode">Live Off-site Auction with Online Bidding</div>
      <div class="begins">Begins: <span>Tuesday, December 23, 2014 at 1:00 PM EST</span></div>
      <div class="loc"><b>Location:</b>P.O. Box 41207<br>Maryville, TN 37801</div>
    </div>
    <div class="bid-btn">Click Here for Online Bidding
      <svg width="24" height="20" viewBox="0 0 24 20"><rect x="1.5" y="1.5" width="21" height="13" fill="none" stroke="#fff" stroke-width="2"/><path d="M8 19 H16 M12 15 V19" stroke="#fff" stroke-width="2"/></svg></div>
  </article>

  <article class="auction-card">
    <h3>Lorem ipsum dolor sit amet conse ctetur adipisicing</h3>
    <div class="auction-media">
      <div class="auction-photo" role="img" aria-label="Large two-storey family home"></div>
      <div class="details-bar">Click Here for More Details
        <svg width="22" height="22" viewBox="0 0 22 22"><circle cx="12" cy="9" r="6.5" fill="none" stroke="#fff" stroke-width="2.5"/><path d="M7.5 13.5 L2 19.5" stroke="#fff" stroke-width="3"/></svg></div>
    </div>
    <div class="auction-info">
      <h4>Lorem ipsum dolor sit amet conse ctetur adipisicing</h4>
      <p class="summary">Duis aute irure dolor in reprehenderit in voluptate velit esse cillum dolore eu fugiat.</p>
      <hr>
      <div class="mode">Live Off-site Auction with Online Bidding</div>
      <div class="begins">Begins: <span>Tuesday, December 23, 2014 at 1:00 PM EST</span></div>
      <div class="loc"><b>Location:</b>P.O. Box 41207<br>Maryville, TN 37801</div>
    </div>
    <div class="bid-btn">Click Here for Online Bidding
      <svg width="24" height="20" viewBox="0 0 24 20"><rect x="1.5" y="1.5" width="21" height="13" fill="none" stroke="#fff" stroke-width="2"/><path d="M8 19 H16 M12 15 V19" stroke="#fff" stroke-width="2"/></svg></div>
  </article>

  <article class="auction-card">
    <h3>Lorem ipsum dolor sit amet conse ctetur adipisicing</h3>
    <div class="auction-media">
      <div class="auction-photo" role="img" aria-label="Large two-storey family home"></div>
      <div class="details-bar">Click Here for More Details
        <svg width="22" height="22" viewBox="0 0 22 22"><circle cx="12" cy="9" r="6.5" fill="none" stroke="#fff" stroke-width="2.5"/><path d="M7.5 13.5 L2 19.5" stroke="#fff" stroke-width="3"/></svg></div>
    </div>
    <div class="auction-info">
      <h4>Lorem ipsum dolor sit amet conse ctetur adipisicing</h4>
      <p class="summary">Duis aute irure dolor in reprehenderit in voluptate velit esse cillum dolore eu fugiat.</p>
      <hr>
      <div class="mode">Live Off-site Auction with Online Bidding</div>
      <div class="begins">Begins: <span>Tuesday, December 23, 2014 at 1:00 PM EST</span></div>
      <div class="loc"><b>Location:</b>P.O. Box 41207<br>Maryville, TN 37801</div>
    </div>
    <div class="bid-btn">Click Here for Online Bidding
      <svg width="24" height="20" viewBox="0 0 24 20"><rect x="1.5" y="1.5" width="21" height="13" fill="none" stroke="#fff" stroke-width="2"/><path d="M8 19 H16 M12 15 V19" stroke="#fff" stroke-width="2"/></svg></div>
  </article>
</main>

<div class="results-count">Showing 4 of 20 results</div>
<div class="pager" style="left:606px;top:2436px"><span class="current">1</span><span>2</span><span>Next</span></div>

<aside class="sidebar">
  <section class="widget" style="top:0;height:103px">
    <h2>Search Auctions</h2>
    <div class="search-row"><span class="field">Search Here...</span><span class="go">Go</span></div>
  </section>

  <section class="widget featured" style="top:135px;height:423px">
    <h2 style="text-align:left">Upcoming Auctions</h2>
    <h5>Lorem ipsum dolor sit amet</h5>
    <div class="featured-photo" role="img" aria-label="Luxury villa with pool"></div>
    <div class="name">Lorem ipsum</div>
    <p>Praesent tibulum molestie lacueenan udotonmera yhe ndr erit mauris ketyade. Mtaytyasera ...</p>
    <span class="more-btn">Want To see more? Click Here</span>
  </section>

  <section class="widget" style="top:588px;height:306px">
    <h2>Register for Online Bidding</h2>
    <p class="note" style="margin-bottom:14px">Not yet registered? Register Now. Just fill in the form.</p>
    <span class="field">Your Name</span>
    <span class="field" style="margin-top:14px">Your Email id</span>
    <span class="field" style="margin-top:14px">Your Phone No.</span>
    <span class="btn-navy" style="margin-top:14px">Submit</span>
    <p class="note" style="margin-top:12px">Already registered? <span style="color:var(--link)">Sign In</span></p>
  </section>

  <section class="widget" style="top:910px;height:170px">
    <h2>Email Subscription</h2>
    <p class="note" style="margin-bottom:14px">Want to get monthly update? Subscribe us.</p>
    <span class="field">Your email id</span>
    <span class="btn-navy" style="margin-top:12px">Submit</span>
  </section>

  <section class="widget" style="top:1106px;height:436px">
    <h2>Testimonials</h2>
    <div class="testimonial">
      <h6>Lena Marsh</h6>
      <p>Praesent tibulum molestie lacueenan udotonmera yhe ndr erit mauris ketyade. Mtaytyasera molestie tibulum molestie lacueenan haselius porta...</p>
      <a>Read More</a>
    </div>
    <div class="testimonial">
      <h6>Lena Marsh</h6>
      <p>Praesent tibulum molestie lacueenan udotonmera yhe ndr erit mauris ketyade. Mtaytyasera molestie tibulum molestie lacueenan haselius porta...</p>
      <a>Read More</a>
    </div>
    <div class="testimonial">
      <h6>Lena Marsh</h6>
      <p>Praesent tibulum molestie lacueenan udotonmera yhe ndr erit mauris ketyade. Mtaytyasera molestie tibulum molestie lacueenan haselius porta...</p>
      <a>Read More</a>
    </div>
  </section>
</aside>

<footer class="site-footer">
  <div class="footer-col" style="left:78px">
    <h2>Our Associates</h2>
    <div class="assoc-badges" aria-label="Association badges">
      <span style="width:72px"></span><span style="width:46px"></span><span style="width:96px"></span><span style="width:40px"></span>
    </div>
  </div>
  <div class="footer-col footer-contact" style="left:453px">
    <h2>Contact Us</h2>
    <p class="gap">Unit 8, 214 Calder Lane<br>Knoxville, TN<br>United States</p>
    <p class="gap">Email: <a>info@brennauctions.com</a><br>Website: <a>www.brennauctions.com</a></p>
  </div>
  <div class="footer-brand"><span class="brand-mark"></span><span class="brand-name">Brenn</span></div>
  <div class="footer-col" style="left:963px">
    <h2>Get In Touch With Us</h2>
    <div class="footer-social"><span></span><span></span><span></span></div>
  </div>
  <div class="copyright">© 2014, All Rights Reserved</div>
</footer>

</body>
</html>
```